Quiet Harbors : Wasp Trap 19x7.5x31cm ( USE THE DIELIENES)

We are seeking a creative and skilled designer to create an innovative packaging design for our brand "Quiet Harbors," which specializes in eco-friendly, safe, and effective pest control solutions. Our brand Quiet Harbors is deeply rooted in sustainability, safety, and enhancing the living environment, and we aim to communicate these values through our packaging design.

Please take a look at the files for the cuttinglines ( dielines) and futher info about the brand and product. Please make the custom packacking in dutch ( MAKE IN DUTCH)

Target Market(s)

See Brankbook

Industry/Entity Type

See Brankbook

Colors
00AB8E
00BBA5
67D7C9
C6EFE9
E9F9F6

Requirements
Must have
• See Brankbook
Nice to have
• See Brankbook
Should not have
• See Brankbook

```html
<!DOCTYPE html>
<html lang="nl">
<head>
<meta charset="utf-8">
<title>Quiet Harbors – Wespen Lijmval verpakking</title>
<link href="https://fonts.googleapis.com/css2?family=Poppins:wght@300;400;600;700&display=swap" rel="stylesheet">
<style>
  :root {
    --bg: #e4e3e4;
    --white: #fbfbfb;
    --panel-green: #98bd93;
    --panel-green-dark: #84a982;
    --brand-green: #2eaa62;
    --ink: #1f3d36;
    --lime: #c4e62a;
    --camo-dark: #2f5d2c;
    --camo-mid: #5c9a3a;
    --alert-red: #d6332f;
  }
  * { box-sizing: border-box; margin: 0; padding: 0; }
  html, body { width: 1200px; height: 894px; overflow: hidden; }
  body {
    background: var(--bg);
    font-family: "Poppins", sans-serif;
    color: var(--ink);
    display: flex;
    align-items: center;
    justify-content: center;
  }
  .dieline { display: flex; height: 680px; box-shadow: 0 10px 30px rgba(0,0,0,.12); }
  .panel { height: 100%; position: relative; overflow: hidden; }

  /* Front panel */
  .front { width: 290px; background: var(--white); }
  .front .brand {
    position: absolute; left: 22px; top: 42px;
    display: flex; align-items: center; gap: 8px;
  }
  .brand-square { width: 18px; height: 18px; background: var(--brand-green); }
  .brand-name { font-weight: 700; font-size: 15px; line-height: 1.05; color: var(--ink); }
  .product-visual {
    position: absolute; right: 0; top: 80px; width: 130px; bottom: 0;
    background: linear-gradient(90deg, var(--lime) 0%, var(--camo-mid) 35%, var(--camo-dark) 60%, var(--camo-mid) 80%, var(--lime) 100%);
  }
  .front .title-block { position: absolute; left: 22px; top: 240px; }
  .count-tag {
    display: inline-block; background: var(--brand-green); color: #fff;
    font-weight: 600; font-size: 17px; padding: 6px 10px; margin-bottom: 10px;
  }
  .title-main { font-weight: 700; font-size: 28px; line-height: 1.1; }
  .title-sub { font-weight: 300; font-size: 26px; line-height: 1.1; }
  .pest-icons { position: absolute; left: 22px; bottom: 40px; display: flex; gap: 8px; }

  /* Tagline side */
  .side { width: 220px; background: linear-gradient(180deg, var(--panel-green), var(--panel-green-dark)); display: flex; align-items: center; justify-content: center; }
  .tagline {
    font-weight: 300; font-size: 15px; line-height: 1.55; text-align: center;
    color: var(--ink); padding: 0 20px;
  }

  /* Info side */
  .info { width: 240px; background: var(--panel-green); }
  .info-head { display: flex; justify-content: space-between; padding: 30px 18px 0; }
  .info-title { font-weight: 600; font-size: 14px; line-height: 1.1; }
  .info-title span { display: block; font-weight: 300; }
  .info-brand { font-weight: 400; font-size: 9px; color: #f2f7f0; }
  .info-body { padding: 28px 18px 0 22px; }
  .section-head {
    font-weight: 600; font-size: 8px; border-left: 5px solid var(--brand-green);
    padding-left: 4px; margin-bottom: 6px;
  }
  .info-list { list-style: none; font-size: 7px; line-height: 1.45; margin-bottom: 16px; }
  .info-list li { position: relative; padding-left: 8px; margin-bottom: 5px; }
  .info-list li::before { content: ""; position: absolute; left: 0; top: 3px; width: 3px; height: 3px; background: var(--ink); }
  .badges { display: flex; gap: 6px; justify-content: center; margin-top: 6px; }
  .badge { width: 18px; height: 18px; border-radius: 50%; border: 2px solid var(--brand-green); background: #e9f5ea; }
  .warning { font-size: 4.5px; font-weight: 600; text-align: center; margin-top: 6px; }
  .scene-photo {
    position: absolute; left: 0; right: 0; bottom: 0; height: 245px;
    background: linear-gradient(160deg, #b7cfa8 0%, #5f7c45 45%, #3c4a30 75%, #6b7a4d 100%);
  }
  .recycle-marks { position: absolute; right: 14px; bottom: 14px; display: flex; gap: 4px; }
  .recycle-marks span { width: 12px; height: 12px; border: 1px solid #eee; }
</style>
</head>
<body>
  <main class="dieline">
    <section class="panel front">
      <div class="brand"><span class="brand-square"></span><span class="brand-name">Quiet<br>Harbors</span></div>
      <div class="product-visual" role="img" aria-label="Productfoto van de groene wespenval met camouflageprint"></div>
      <div class="title-block">
        <div class="count-tag">2 Stuks</div>
        <div class="title-main">Wespen</div>
        <div class="title-sub">Lijmval</div>
      </div>
      <div class="pest-icons">
        <svg width="20" height="20" viewBox="0 0 20 20"><circle cx="10" cy="10" r="8" fill="none" stroke="var(--alert-red)" stroke-width="2"/><line x1="4" y1="4" x2="16" y2="16" stroke="var(--alert-red)" stroke-width="2"/></svg>
        <svg width="20" height="20" viewBox="0 0 20 20"><circle cx="10" cy="10" r="8" fill="none" stroke="var(--alert-red)" stroke-width="2"/><line x1="4" y1="4" x2="16" y2="16" stroke="var(--alert-red)" stroke-width="2"/></svg>
        <svg width="20" height="20" viewBox="0 0 20 20"><circle cx="10" cy="10" r="8" fill="none" stroke="var(--alert-red)" stroke-width="2"/><line x1="4" y1="4" x2="16" y2="16" stroke="var(--alert-red)" stroke-width="2"/></svg>
      </div>
    </section>

    <section class="panel side">
      <p class="tagline">Bij Quiet Harbors hechten we waarde aan effectieve bestrijding, om de veiligheid van iedereen in jouw omgeving te garanderen</p>
    </section>

    <section class="panel info">
      <div class="info-head">
        <div class="info-title">Wespen<span>Lijmval</span></div>
        <div class="info-brand">Quiet Harbors</div>
      </div>
      <div class="info-body">
        <div class="section-head">Eigenschappen</div>
        <ul class="info-list">
          <li>Veilig voor allen: Lijm zonder gif, beschermt zonder zorgen.</li>
          <li>Klik &amp; Klaar: Supersnelle setup, ideaal voor elk hoekje buiten.</li>
          <li>Groen Gedacht: Vriendelijk voor milieu, gericht op vliegende beesten.</li>
          <li>Stijlvol ontwerp: Gaat op in de omgeving zonder af te leiden.</li>
        </ul>
        <div class="section-head">Jouw Voordeel</div>
        <ul class="info-list">
          <li>Buitenleven zonder wespenstress.</li>
          <li>Zeg vaarwel tegen stekende verrassingen.</li>
          <li>Boost voor biodiversiteit.</li>
          <li>Bespaar flink op ongediertebestrijding.</li>
        </ul>
        <div class="badges"><span class="badge"></span><span class="badge"></span><span class="badge"></span><span class="badge"></span></div>
        <p class="warning">Let op: buiten bereik van kinderen en huisdieren houden</p>
      </div>
      <div class="scene-photo" role="img" aria-label="Foto van de wespenval hangend aan een boom in een tuin">
        <div class="recycle-marks"><span></span><span></span></div>
      </div>
    </section>
  </main>
</body>
</html>
```